Fielduro home page and search results web design

We are looking for an attractive front page and search page for our website, Fielduro.us. The site is currently up and can be searched. Most of the functionality works, but the design needs to be improved. The website is a platform that allows sports facility managers to list their facilities and allow the public to rent them. Can be thought of as the DineSlot for athletic facilities. The 2 pages we would like designed are the home page, where a renter would search for a facility, and the search results page, where there is a map of the facilities available on the left and the available facility listings on the right.

Target Market(s)

Sports facility managers and sports organizations

Number of Pages Required

2 page

Colors

Designer to choose colors to be used in the design.

Requirements
Must have
• Be very easy for someone visiting the site to use.

```html
<!DOCTYPE html>
<html lang="en">
<head>
<meta charset="utf-8">
<title>Fielduro – Home</title>
<link href="https://fonts.googleapis.com/css2?family=Open+Sans:wght@400;600;700&display=swap" rel="stylesheet">
<style>
:root{
  --green:#7cc142;
  --green-dark:#5f9e2c;
  --ink:#222;
  --muted:#666;
  --line:#e4e4e4;
  --hero:#3b3f37;
  --band:#4a4a4a;
  --light:#eeeeee;
  --footer:#2b2b2b;
  --footer-bar:#333;
  --footer-base:#232323;
  --white:#fff;
}
*{box-sizing:border-box;margin:0;padding:0}
html,body{width:1200px;height:1200px;overflow:hidden;background:#fff;font-family:"Open Sans",Arial,sans-serif;color:var(--ink)}
.page{position:absolute;left:335px;top:48px;width:662px;height:1380px;transform:scale(.8);transform-origin:0 0;background:#fff;box-shadow:0 0 6px rgba(0,0,0,.18);overflow:hidden}
.abs{position:absolute}
.brand{font-weight:700;font-size:13px;color:var(--ink);display:flex;align-items:center;gap:4px;letter-spacing:.2px}
.brand .dot{width:8px;height:8px;border-radius:50%;background:var(--green)}
.header{left:0;top:0;width:662px;height:31px;background:#fff}
.nav a{position:absolute;top:12px;font-size:5px;font-weight:600;color:#333;text-decoration:none;letter-spacing:.3px}
.nav .sep{position:absolute;left:318px;top:9px;width:1px;height:13px;background:var(--line)}
.login{left:438px;top:12px;font-size:5px;color:#333;display:flex;align-items:center;gap:2px}
.login i{width:4px;height:4px;background:var(--green);display:inline-block;border-radius:1px}
.btn-outline{border:1.3px solid var(--green);border-radius:8px;font-size:5px;color:#333;text-align:center}
.hero{left:0;top:31px;width:662px;height:211px;background:linear-gradient(180deg,#4a4d43 0%,#3b3f36 55%,#3d332c 100%)}
.hero h1{left:0;width:662px;top:71px;text-align:center;color:#fff;font-size:12.5px;font-weight:600;letter-spacing:.3px}
.hero p{left:0;width:662px;top:89px;text-align:center;color:#ddd;font-size:5.5px}
.field{top:116px;width:87px;height:19px;border:1px solid rgba(255,255,255,.55);background:rgba(255,255,255,.08);font-size:4.5px;color:#eee;padding:6px 6px}
.search-btn{left:448px;top:116px;width:46px;height:19px;background:var(--green);color:#fff;font-size:4.5px;font-weight:700;display:flex;align-items:center;justify-content:center;gap:3px}
.section-title{left:0;width:662px;text-align:center;font-weight:700;font-size:12px;color:var(--ink);letter-spacing:.2px}
.lead{left:170px;width:322px;text-align:center;font-size:5.5px;line-height:9.5px;color:var(--muted)}
.feature{width:211px;height:70px;padding:12px 10px 0 46px}
.feature.active{background:#fff;box-shadow:0 1px 5px rgba(0,0,0,.2)}
.feature .icon{position:absolute;left:8px;top:13px;width:28px;height:28px;border-radius:50%;background:var(--green);display:flex;align-items:center;justify-content:center}
.feature h3{font-size:7px;font-weight:700;margin-bottom:5px}
.feature p{font-size:4.3px;line-height:8.2px;color:var(--muted)}
.band{left:0;top:533px;width:662px;height:153px;background:linear-gradient(90deg,#3e3e3e,#555 60%,#4a4a4a)}
.band h2{left:0;width:662px;top:69px;text-align:center;color:#fff;font-size:12px;font-weight:700;letter-spacing:.2px}
.card{top:642px;width:133px;height:163px;background:#fff;border:1px solid #eee}
.card.lift{box-shadow:0 1px 5px rgba(0,0,0,.22)}
.card .photo{height:80px}
.card h4{position:absolute;left:13px;top:91px;font-size:5.5px;font-weight:700}
.card .addr{position:absolute;left:13px;top:102px;font-size:4.3px;color:var(--muted);display:flex;gap:3px;align-items:center}
.card .stars{position:absolute;left:13px;top:118px;font-size:6px;letter-spacing:.3px;color:#f2641a}
.card .stars span{color:#ccc}
.card .price{position:absolute;left:13px;top:136px;font-size:10px;font-weight:700}
.card .price em{font-size:5px;font-weight:400;margin-left:2px}
.community{left:0;top:835px;width:662px;height:255px;background:var(--light)}
.community .sub{left:0;width:662px;top:53px;text-align:center;font-size:5.5px;color:var(--muted)}
.quote{left:121px;top:88px;width:204px;height:79px;background:#fff;padding:12px 14px}
.quote h5{font-size:5.5px;font-weight:700;margin-bottom:8px}
.quote p{font-size:4.3px;line-height:8.3px;color:var(--muted)}
.quote .tail{position:absolute;left:28px;bottom:-7px;width:0;height:0;border-left:6px solid transparent;border-right:6px solid transparent;border-top:7px solid #fff}
.avatar{left:132px;top:185px;width:36px;height:36px;border-radius:50%;background:linear-gradient(160deg,#9fb3c2,#6f8496);border:2px solid #fff}
.person{left:178px;top:195px;font-size:5.5px;font-weight:700}
.person span{display:block;font-size:4.5px;font-weight:400;color:var(--muted);margin-top:2px}
.video{left:336px;top:88px;width:203px;height:133px;background:radial-gradient(circle at 55% 45%,#8a8f8f,#5e6566 70%)}
.play{left:86px;top:50px;width:31px;height:31px;border-radius:50%;border:1.5px solid #fff;background:rgba(0,0,0,.25)}
.account{left:0;top:1090px;width:662px;height:95px;background:#fff}
.footer{left:0;top:1185px;width:662px;height:195px;background:var(--footer);color:#bbb}
.footer h6{position:absolute;top:29px;font-size:7px;font-weight:700;color:#fff}
.footer .txt{position:absolute;font-size:4.3px;line-height:8.3px;color:#aaa}
.tag{position:absolute;height:12px;border:1.2px solid var(--green);border-radius:7px;font-size:4.3px;color:#ccc;text-align:center;line-height:9.5px}
.foot-bar{left:0;top:125px;width:662px;height:40px;background:var(--footer-bar)}
.social{position:absolute;top:14px;width:12px;height:12px;border-radius:50%;background:#fff}
.foot-search{left:441px;top:14px;width:80px;height:12px;border:1px solid #777;border-radius:7px;font-size:4.3px;color:#888;padding:2px 7px}
.copy{left:0;top:165px;width:662px;height:30px;background:var(--footer-base);font-size:4.3px;color:#888;text-align:center;line-height:30px}
</style>
</head>
<body>
<div class="page">

  <header class="abs header">
    <div class="abs brand" style="left:119px;top:8px"><span>Fielduro</span><span class="dot"></span></div>
    <nav class="nav">
      <a style="left:280px">RENTERS</a>
      <span class="sep"></span>
      <a style="left:328px">FACILITY MANAGER</a>
    </nav>
    <div class="abs login"><i></i>Login</div>
    <div class="abs btn-outline" style="left:468px;top:8px;width:53px;height:14px;line-height:11px">Add my listing</div>
    <div class="abs" style="left:527px;top:9px;width:13px;height:13px;border:1.3px solid var(--green);border-radius:50%">
      <svg width="10" height="10" viewBox="0 0 10 10" style="position:absolute;left:0.5px;top:0.5px"><circle cx="4.5" cy="4.5" r="2" fill="none" stroke="#333" stroke-width=".9"/><line x1="6" y1="6" x2="7.5" y2="7.5" stroke="#333" stroke-width=".9"/></svg>
    </div>
  </header>

  <section class="abs hero" role="img" aria-label="Tennis player serving on an outdoor court at dusk">
    <h1 class="abs">Search &amp; Resere Facilities</h1>
    <p class="abs">or create your own listing today...</p>
    <div class="abs field" style="left:168px">City</div>
    <div class="abs field" style="left:262px">State</div>
    <div class="abs field" style="left:356px">Zip code</div>
    <div class="abs search-btn">
      <svg width="6" height="6" viewBox="0 0 10 10"><circle cx="4" cy="4" r="3" fill="none" stroke="#fff" stroke-width="1.4"/><line x1="6.2" y1="6.2" x2="9" y2="9" stroke="#fff" stroke-width="1.4"/></svg>SEARCH
    </div>
  </section>

  <h2 class="abs section-title" style="top:278px">Facilities Management Portal</h2>
  <p class="abs lead" style="top:303px">Reserv a facility that suits you, for your practicies, tournamnets and events. Never struggle to find facilities for your practices, book in advance for a nominal price.</p>

  <div class="abs feature active" style="left:114px;top:347px">
    <div class="icon"><svg width="14" height="14" viewBox="0 0 14 14"><circle cx="5" cy="8" r="3" fill="none" stroke="#fff" stroke-width="1.2"/><circle cx="10" cy="4" r="2" fill="none" stroke="#fff" stroke-width="1.2"/></svg></div>
    <h3>How it Works</h3>
    <p>Fielduro is an online platform and marketplace for people to list, discover, and book facilities for sports activities. Fielduro utilises a network of local Sports Organizations, Facility Owners and affiliates to list and manage their facilities on the platform.</p>
  </div>
  <div class="abs feature" style="left:338px;top:347px">
    <div class="icon"><svg width="14" height="14" viewBox="0 0 14 14"><circle cx="7" cy="7" r="5" fill="none" stroke="#fff" stroke-width="1.2"/><circle cx="7" cy="7" r="2.3" fill="none" stroke="#fff" stroke-width="1.2"/></svg></div>
    <h3>Renters</h3>
    <p>Renters can browse listings and filter by location, type of facility, or keyword. Once users find a facility they like, they can reserv the facility online. Finally, the renter receives a confirmation and have an unforgettable event!</p>
  </div>
  <div class="abs feature" style="left:114px;top:428px">
    <div class="icon"><svg width="14" height="14" viewBox="0 0 14 14"><circle cx="7" cy="4.5" r="2.5" fill="none" stroke="#fff" stroke-width="1.2"/><rect x="3" y="8.5" width="8" height="4" rx="1" fill="none" stroke="#fff" stroke-width="1.2"/></svg></div>
    <h3>Owners</h3>
    <p>Fielduro owners add facility information, location, pictures, availability, pricing ... When an renter reserves a facility, the owner will verify any doc requirements and confirm or reject a reservation and accept payment.</p>
  </div>
  <div class="abs feature" style="left:338px;top:428px">
    <div class="icon"><svg width="16" height="14" viewBox="0 0 16 14"><path d="M1 7 L5 3 L8 6 L11 3 L15 7 L8 12 Z" fill="none" stroke="#fff" stroke-width="1.2" stroke-linejoin="round"/></svg></div>
    <h3>Benefits</h3>
    <p>Manage your facilities online and earn more income. Fielduro will handle back end details to guarantee a safe and secure exchange all around. Fielduro will also facilitate reviews following the event.</p>
  </div>

  <section class="abs band" role="img" aria-label="Laptop on a desk showing the site, with a potted plant behind">
    <h2 class="abs">Featured Facilities</h2>
  </section>

  <article class="abs card lift" style="left:122px">
    <div class="photo" role="img" aria-label="Aerial view of an indoor soccer complex among trees" style="background:linear-gradient(160deg,#6f8f4e,#4c6b3a 60%,#7a8a6a)"></div>
    <h4>Indoor Soccer Field</h4>
    <div class="addr"><svg width="5" height="6" viewBox="0 0 10 12"><path d="M5 11 C2 7 1 5.5 1 4 a4 4 0 0 1 8 0 c0 1.5-1 3-4 7z" fill="none" stroke="#7cc142" stroke-width="1.4"/></svg>Cedar Hollow, Texas 75000</div>
    <div class="stars">★★★★<span>★</span></div>
    <div class="price">$50<em>per hour</em></div>
  </article>
  <article class="abs card" style="left:264px">
    <div class="photo" role="img" aria-label="Indoor basketball arena with wooden court" style="background:linear-gradient(180deg,#6b4a2e,#b98a4f 55%,#8a3a2a)"></div>
    <h4>Indoor Field</h4>
    <div class="addr"><svg width="5" height="6" viewBox="0 0 10 12"><path d="M5 11 C2 7 1 5.5 1 4 a4 4 0 0 1 8 0 c0 1.5-1 3-4 7z" fill="none" stroke="#7cc142" stroke-width="1.4"/></svg>Cedar Hollow, Texas 75000</div>
    <div class="stars">★★★<span>★★</span></div>
    <div class="price">$60<em>per hour</em></div>
  </article>
  <article class="abs card" style="left:407px">
    <div class="photo" role="img" aria-label="Aerial view of outdoor football and baseball fields" style="background:linear-gradient(150deg,#7a5a3a,#4f6e3e 45%,#6d8a5a)"></div>
    <h4>Indoor Field</h4>
    <div class="addr"><svg width="5" height="6" viewBox="0 0 10 12"><path d="M5 11 C2 7 1 5.5 1 4 a4 4 0 0 1 8 0 c0 1.5-1 3-4 7z" fill="none" stroke="#7cc142" stroke-width="1.4"/></svg>Cedar Hollow, Texas 75000</div>
    <div class="stars">★★★★★</div>
    <div class="price">$80<em>per hour</em></div>
  </article>

  <section class="abs community">
    <h2 class="abs section-title" style="top:30px">Meet Our Community</h2>
    <p class="abs sub">See what people are saying about Fielduro.</p>
    <svg class="abs" style="left:86px;top:143px" width="12" height="24" viewBox="0 0 12 24"><path d="M11 1 L1 12 L11 23" fill="none" stroke="#333" stroke-width="1.2"/></svg>
    <svg class="abs" style="left:565px;top:143px" width="12" height="24" viewBox="0 0 12 24"><path d="M1 1 L11 12 L1 23" fill="none" stroke="#333" stroke-width="1.2"/></svg>
    <div class="abs quote">
      <h5>Miles Carter</h5>
      <p>It has been such a great experience to have found this website. Since we have listed our clientelle's businesses here, we have seen a steady uproar of traffic from local users looking for our client's businesses.</p>
      <span class="tail"></span>
    </div>
    <div class="abs avatar" role="img" aria-label="Portrait of the reviewer"></div>
    <div class="abs person">Miles Carter<span>Facility Manager</span></div>
    <div class="abs video" role="img" aria-label="Video testimonial from a smiling man">
      <div class="abs play"><svg width="28" height="28" viewBox="0 0 28 28"><path d="M11 9 L19 14 L11 19 Z" fill="#fff"/></svg></div>
    </div>
  </section>

  <section class="abs account">
    <h2 class="abs section-title" style="top:28px">Create Your Acount</h2>
    <div class="abs btn-outline" style="left:300px;top:53px;width:62px;height:18px;line-height:15px;border-color:#333;border-radius:9px;font-weight:600">Sign Up Now</div>
  </section>

  <footer class="abs footer">
    <h6 style="left:122px">About us</h6>
    <p class="txt" style="left:122px;top:47px;width:142px">Lorem Ipsum is simply dummy text of the printing and typesetting industry. Lorem Ipsum has been the industry's standard dummy text ever since the 1500s, when an unknown printer took a galley of type and scrambled it to make a type specimen book.</p>
    <h6 style="left:291px">Tags</h6>
    <span class="tag" style="left:291px;top:46px;width:30px">Sport</span>
    <span class="tag" style="left:326px;top:46px;width:36px">Baseball</span>
    <span class="tag" style="left:367px;top:46px;width:36px">Renters</span>
    <span class="tag" style="left:291px;top:64px;width:36px">Owners</span>
    <span class="tag" style="left:332px;top:64px;width:32px">Indoor</span>
    <span class="tag" style="left:369px;top:64px;width:29px">Field</span>
    <span class="tag" style="left:291px;top:83px;width:32px">Soccer</span>
    <span class="tag" style="left:328px;top:83px;width:36px">Owners</span>
    <h6 style="left:470px">Useful link</h6>
    <p class="txt" style="left:470px;top:47px">About us<br>Search<br>Renters<br>Facility Manager<br>Subscription<br>Login</p>

    <div class="abs foot-bar">
      <span class="social" style="left:122px"></span>
      <span class="social" style="left:139px"></span>
      <span class="social" style="left:156px"></span>
      <span class="social" style="left:172px"></span>
      <div class="abs brand" style="left:303px;top:11px;color:#fff"><span>Fielduro</span><span class="dot"></span></div>
      <div class="abs foot-search">Search</div>
    </div>
    <div class="abs copy">Copyright © 2017 Brevane Group Inc. All rights reserved.</div>
  </footer>

</div>
</body>
</html>
```